Tall Fern Software PowerPoint template

We are a software company selling endpoint visibility, access and security technology to enterprise-level IT departments.
Our technology helps organizations gain comprehensive visibility into and control over devices accessing their corporate network so they can quickly identify and address suspicious activity on the network that could lead to potential threats like data breaches.
This technology can cost organizations upwards of $1M - depending on the size of the organization. Our primary clients are Marquee 3,000 companies.
We want a professional, polished PowerPoint template that we can use for all company presentations. Please include:
Title page
Section page
General info page
Thank you page
Logo options and color specs are attached.
Please include our tagline on at least the title page: Chart the frontier. Steady the core.
Software

```html
<!DOCTYPE html>
<html lang="en">
<head>
<meta charset="utf-8">
<title>Tall Fern Software – Presentation Template</title>
<link rel="stylesheet" href="https://fonts.googleapis.com/css2?family=Oswald:wght@400;500&family=Open+Sans:wght@400;600;700&display=swap">
<style>
:root{
  --crimson:#8e181d;
  --crimson-deep:#861419;
  --copper:#d4784f;
  --salmon:#d98a66;
  --blush:#f3d2c2;
  --ink:#555;
  --grey:#777;
  --page:#ffffff;
  --steel-a:#c9d6de;
  --steel-b:#3c5a73;
  --sky-a:#d6e8f5;
  --sky-b:#3f8fc8;
  --office-a:#e8e2dc;
  --office-b:#8a7466;
  --room-a:#f4f4f2;
  --room-b:#9aa39a;
}
*{box-sizing:border-box;margin:0;padding:0}
html,body{width:1200px;height:1071px;overflow:hidden;background:var(--page)}
body{position:relative;font-family:"Open Sans",Arial,sans-serif;color:var(--ink)}
.slide{position:absolute;width:538px;height:302px;background:#fff;overflow:hidden;box-shadow:0 1px 7px rgba(0,0,0,.35)}
.col-l{left:41px}.col-r{left:621px}
.row-1{top:35px}.row-2{top:377px}.row-3{top:723px}

.brand{position:absolute;display:flex;align-items:center;gap:8px;color:var(--crimson);font-weight:700;line-height:1.05;letter-spacing:2px;text-transform:uppercase}
.brand .mark{width:10px;height:10px;background:var(--copper)}
.brand .name{font-size:13px}
.brand .name span{display:block;font-size:8px;letter-spacing:3.4px}

.photo{position:absolute}
.heading{position:absolute;z-index:2;font-size:21px;line-height:1.2;font-weight:400;color:var(--ink)}
.heading b{color:var(--crimson);font-weight:700}
.lead{position:absolute;font-size:8.4px;line-height:1.3;color:var(--copper)}
.body{position:absolute;font-size:7.6px;line-height:1.3;color:var(--grey)}

/* title */
.title .brand{left:40px;top:45px}
.title .photo{left:270px;top:0;width:268px;height:302px;background:linear-gradient(160deg,var(--steel-a),#8ea6b8 45%,var(--steel-b))}
.title .tagline-a{position:absolute;left:0;width:270px;top:118px;text-align:center;font-family:"Oswald",sans-serif;font-size:29px;line-height:1.2;color:var(--copper);font-weight:400}
.title .rule{position:absolute;left:22px;width:226px;top:168px;height:2px;background:var(--crimson)}
.title .tagline-b{position:absolute;left:0;width:270px;top:178px;text-align:center;font-family:"Oswald",sans-serif;font-size:15.5px;line-height:1.2;color:var(--crimson);font-weight:500}
.title .body{left:34px;width:202px;top:228px;text-align:center}

/* image slide */
.image-slide .heading{left:21px;top:9px}
.image-slide .lead{left:21px;top:64px;width:212px}
.image-slide .body{left:21px;top:128px;width:180px}
.image-slide .brand{left:21px;top:268px}
.image-slide .brand .name{font-size:11px}.image-slide .brand .name span{font-size:7px}
.image-slide .photo{inset:0;background:linear-gradient(180deg,#fff 0%,var(--sky-a) 35%,var(--sky-b) 100%);clip-path:polygon(276px 0,538px 0,538px 302px,196px 302px)}
.image-slide svg{position:absolute;left:0;top:0}

/* contents */
.contents .heading{left:21px;top:11px}
.contents .body{left:21px;top:58px;width:470px;font-size:8px}
.toc{position:absolute;left:21px;top:107px;display:grid;grid-template-columns:161px 170px 150px;row-gap:17px}
.toc li{list-style:none;display:flex;align-items:center;gap:11px;font-size:7px;font-weight:600;color:var(--copper)}
.toc li i{width:20px;height:20px;background:var(--crimson);color:#fff;font-style:normal;font-size:6.5px;display:flex;align-items:center;justify-content:center}
.contents .brand{left:400px;top:266px}
.contents .brand .name{font-size:11px}.contents .brand .name span{font-size:7px}

/* about */
.about .photo{left:0;top:0;width:328px;height:302px;background:linear-gradient(135deg,var(--office-a),#c9b3a3 50%,var(--office-b))}
.about .heading{left:344px;top:13px}
.about .lead{left:344px;top:45px;width:160px}
.about .body{left:344px;top:130px;width:178px;padding-left:4px;border-left:2px solid var(--crimson)}
.about .body p+p{margin-top:8px}
.about .brand{left:344px;top:269px}
.about .brand .name{font-size:11px}.about .brand .name span{font-size:7px}

/* testimonials */
.testimonials .photo{left:0;top:44px;width:260px;height:258px;background:radial-gradient(ellipse at 45% 50%,var(--room-a) 30%,#d5d8d3 60%,var(--room-b))}
.testimonials .panel{position:absolute;inset:0;background:var(--salmon);clip-path:polygon(280px 0,538px 0,538px 302px,193px 302px)}
.testimonials svg{position:absolute;left:0;top:0}
.testimonials .heading{left:21px;top:9px}
.testimonials .quote{position:absolute;left:274px;top:72px;width:232px;color:#fff;font-size:10px;line-height:1.32;text-align:center}
.testimonials .quote p+p{margin-top:10px}
.testimonials .mark-q{position:absolute;color:#fff;font-family:Georgia,serif;font-size:42px;font-weight:700;line-height:1}
.testimonials .author{position:absolute;left:274px;width:232px;top:254px;text-align:center;font-size:8.5px;font-weight:600;color:var(--crimson)}

/* thanks */
.thanks .band{position:absolute;left:0;top:0;width:538px;height:171px;background:var(--crimson-deep);border-bottom:4px solid var(--salmon)}
.thanks .big{position:absolute;left:50px;top:40px;font-family:"Oswald",sans-serif;font-size:42px;line-height:1.2;font-weight:500;color:var(--copper);letter-spacing:.5px}
.thanks .big span{color:var(--blush)}
.thanks .rule{position:absolute;left:58px;top:104px;width:162px;height:1px;background:rgba(255,255,255,.55)}
.thanks .cta{position:absolute;left:58px;width:162px;top:113px;text-align:center;font-size:11px;font-weight:700;color:#fff}
.thanks .divider{position:absolute;left:273px;top:15px;width:1px;height:142px;background:rgba(255,255,255,.45)}
.thanks .contact{position:absolute;left:313px;top:70px;color:#fff;font-size:11.5px;line-height:1.45}
.thanks .brand{left:150px;top:211px;gap:14px}
.thanks .brand .mark{width:22px;height:22px}
.thanks .brand .name{font-size:26px;letter-spacing:4px}
.thanks .brand .name span{font-size:14px;letter-spacing:8.6px}
</style>
</head>
<body>

<section class="slide title col-l row-1">
  <div class="brand"><i class="mark"></i><div class="name">Tall Fern<span>Software</span></div></div>
  <h1 class="tagline-a">CHART THE FRONTIER</h1>
  <div class="rule"></div>
  <h2 class="tagline-b">STEADY THE CORE</h2>
  <p class="body">Lorem Ipsum is simply dummy text of the printing and typesetting industry. Lorem Ipsum has been the industry's standard dummy text ever since the 1500s</p>
  <div class="photo" role="img" aria-label="Photo of a modern glass office tower seen from below"></div>
</section>

<section class="slide image-slide col-r row-1">
  <div class="photo" role="img" aria-label="Photo of business people silhouetted on a reflective blue floor"></div>
  <svg width="538" height="302" aria-hidden="true"><polygon points="268,0 276,0 196,302 186,302" fill="#8e181d"/></svg>
  <h2 class="heading">Image <b>Slide</b></h2>
  <p class="lead">Lorem Ipsum is simply dummy text of the printing and typesetting industry. Lorem Ipsum has been the industry's standard dummy text ever since the 1500s.</p>
  <p class="body">Lorem Ipsum is simply dummy text of the printing and typesetting industry. Lorem Ipsum has been the industry's standard dummy text ever since the 1500s.when an unknown printer took a galley of type and scrambled it to make a type specimen book. when an unknown printer took a galley of type and scrambled it to make a type specimen book. It has survived not only five centuries.</p>
  <div class="brand"><i class="mark"></i><div class="name">Tall Fern<span>Software</span></div></div>
</section>

<section class="slide contents col-l row-2">
  <h2 class="heading">Table of <b>Contents</b></h2>
  <p class="body">Lorem Ipsum is simply dummy text of the printing and typesetting industry. Lorem Ipsum has been the industry's standard dummy text ever since the 1500s.</p>
  <ul class="toc">
    <li><i>1</i>Home</li><li><i>5</i>Home</li><li><i>9</i>Home</li>
    <li><i>2</i>About Us</li><li><i>6</i>About Us</li><li><i>10</i>About Us</li>
    <li><i>3</i>Gallery</li><li><i>7</i>Gallery</li><li><i>11</i>Gallery</li>
    <li><i>4</i>Portfolio</li><li><i>8</i>Portfolio</li><li><i>12</i>Portfolio</li>
  </ul>
  <div class="brand"><i class="mark"></i><div class="name">Tall Fern<span>Software</span></div></div>
</section>

<section class="slide about col-r row-2">
  <div class="photo" role="img" aria-label="Photo of a smiling team working together at a desk with a laptop"></div>
  <h2 class="heading">About <b>Us</b></h2>
  <p class="lead">Lorem Ipsum is simply dummy text of the printing and typesetting industry. Lorem Ipsum has been the industry's standard dummy text ever since the 1500s.</p>
  <div class="body">
    <p>Lorem Ipsum is simply dummy text of the printing and typesetting industry. Lorem Ipsum has been the industry's standard dummy text ever since the 1500s.when an unknown printer took a galley of type and scrambled it to make a type specimen book.</p>
    <p>when an unknown printer took a galley of type and scrambled it to make a type specimen book. It has survived not only five centuries.</p>
  </div>
  <div class="brand"><i class="mark"></i><div class="name">Tall Fern<span>Software</span></div></div>
</section>

<section class="slide testimonials col-l row-3">
  <div class="photo" role="img" aria-label="Image of a round meeting table with office chairs and a green sprout growing from its centre"></div>
  <div class="panel"></div>
  <svg width="538" height="302" aria-hidden="true"><polygon points="276,0 282,0 195,302 189,302" fill="#8e181d"/></svg>
  <h2 class="heading">Our <b>Testimonials</b></h2>
  <span class="mark-q" style="left:250px;top:52px">“</span>
  <div class="quote">
    <p>Lorem Ipsum is simply dummy text of the printing and typesetting industry. Lorem Ipsum has been the industry's standard dummy text ever since the 1500s.when an unknown printer took a galley of type and scrambled it to make a type specimen book.</p>
    <p>when an unknown printer took a galley of type and scrambled it to make a type specimen book. It has survive centuries.</p>
  </div>
  <span class="mark-q" style="left:502px;top:188px">”</span>
  <p class="author">— Dana Whitlock —</p>
</section>

<section class="slide thanks col-r row-3">
  <div class="band"></div>
  <h2 class="big">THANK <span>YOU</span></h2>
  <div class="rule"></div>
  <p class="cta">SEND YOUR FEEDBACK</p>
  <div class="divider"></div>
  <p class="contact">Email : hello@tallfern.com<br>Web : tallfern.com<br>Tel : 3333-418-207</p>
  <div class="brand"><i class="mark"></i><div class="name">Tall Fern<span>Software</span></div></div>
</section>

</body>
</html>
```